Commercial Construction Company

We need a business card design based on our current logo. We are a commercial general contractor based in Southern California that specializes in bank remodels. We would like to see designs that incorporate dark blue. The final design should portray an image of professionalism and quality.

If possible, I would like to add metallic foil to the design. Thank you

```html
<!DOCTYPE html>
<html lang="en">
<head>
<meta charset="utf-8">
<title>Halvern Commercial Builders – Business Card</title>
<link href="https://fonts.googleapis.com/css2?family=Roboto:wght@400;500;700&display=swap" rel="stylesheet">
<style>
  :root {
    --brand-blue: #134a80;
    --ink: #333a42;
    --muted: #8a8f94;
    --paper: #ffffff;
    --backdrop: #e9e6e1;
  }
  * { box-sizing: border-box; margin: 0; padding: 0; }
  html, body { width: 1200px; height: 700px; overflow: hidden; }
  body {
    background: var(--backdrop);
    font-family: "Roboto", Arial, sans-serif;
    position: relative;
  }
  .card {
    position: absolute;
    width: 540px;
    height: 310px;
    box-shadow: 0 6px 16px rgba(0,0,0,0.25);
  }
  .card--front {
    left: 50px; top: 70px;
    background: var(--brand-blue);
    display: flex; align-items: center; justify-content: center;
  }
  .front-brand {
    display: flex; align-items: center; gap: 14px;
    color: var(--paper);
    font-weight: 700;
    font-size: 40px;
    letter-spacing: 1px;
  }
  .brand-dot {
    width: 22px; height: 22px; border-radius: 50%;
    background: currentColor;
  }
  .card--back {
    left: 610px; top: 320px;
    background: var(--paper);
  }
  .back-brand {
    position: absolute; right: 32px; top: 52px;
    display: flex; align-items: center; gap: 10px;
    color: var(--brand-blue);
    font-weight: 700;
    font-size: 30px;
  }
  .back-brand .brand-dot { width: 16px; height: 16px; }
  .person { position: absolute; left: 33px; top: 172px; }
  .person-name { color: var(--brand-blue); font-weight: 700; font-size: 18px; }
  .person-title { color: var(--muted); font-size: 12.5px; margin-top: 3px; }
  .divider { position: absolute; left: 33px; top: 212px; }
  .contact-list {
    position: absolute; left: 33px; top: 228px;
    list-style: none; color: var(--ink); font-size: 12.5px; line-height: 15.5px;
  }
  .contact-list li { display: flex; align-items: center; gap: 7px; }
  .contact-list svg { width: 10px; height: 10px; fill: var(--brand-blue); }
  .address {
    position: absolute; right: 32px; top: 246px;
    text-align: right; color: var(--ink); font-size: 12.5px; line-height: 15.5px;
  }
</style>
</head>
<body>
  <section class="card card--front">
    <div class="front-brand"><span class="brand-dot"></span>Halvern</div>
  </section>

  <section class="card card--back">
    <div class="back-brand"><span class="brand-dot"></span>Halvern</div>

    <div class="person">
      <div class="person-name">Daniel Reyes</div>
      <div class="person-title">President</div>
    </div>

    <svg class="divider" width="475" height="12" viewBox="0 0 475 12">
      <line x1="0" y1="6" x2="465" y2="6" stroke="#134a80" stroke-width="1.5"/>
      <polygon points="465,1 475,6 465,11" fill="#134a80"/>
    </svg>

    <ul class="contact-list">
      <li><svg viewBox="0 0 10 10"><path d="M2 0.5 L3.8 2.6 L2.9 3.8 C3.6 5.3 4.7 6.4 6.2 7.1 L7.4 6.2 L9.5 8 L8.4 9.5 C4.2 9.2 0.8 5.8 0.5 1.6 Z"/></svg>555-204-1187</li>
      <li><svg viewBox="0 0 10 10"><path d="M2.5 0 H7.5 V10 H2.5 Z M3.5 1 V8 H6.5 V1 Z"/></svg>555-318-6642</li>
      <li><svg viewBox="0 0 10 10"><path d="M2.5 0 H7.5 V3 H2.5 Z M0.5 3.5 H9.5 V10 H0.5 Z M2.5 6 V9 H7.5 V6 Z"/></svg>555-407-2290</li>
      <li><svg viewBox="0 0 10 10"><path d="M0.5 2 H9.5 V8.5 H0.5 Z M1.3 2.6 L5 5.5 L8.7 2.6 Z" fill-rule="evenodd"/></svg>info@halvernbuild.com</li>
    </ul>

    <div class="address">
      <div>2140 Larkspur Avenue</div>
      <div>Irvine, California 92614</div>
      <div>www.halvernbuild.com</div>
    </div>
  </section>
</body>
</html>
```